Website redesign www.brindlecovepc.com law firm site

Need to redesign the website that I currently have to look more modern and professional. Would also like to be able to make updates and post without having a huge hassle. See current www.brindlecovepc.com. I just think that it looks very immature and it's very templated there's no ability for me to make posts or Add links or anything like that

Target Market(s)

California people looking for a powerhouse attorney in

Industry/Entity Type

Legal

Number of Pages Required

3 page

Font styles to use
Serif
Sans Serif

Colors
ec1f27
000000
ffffff

Requirements
Must have
• Must be mobile friendly. Must look professional and have ability to post links to other websites. Must have ability to post blogs or articles. Would like to be able to read my Quindral account and also have the ability to upload forms for people to download
Nice to have
• Simple design easy to use and not cluttered with too much text

```html
<!DOCTYPE html>
<html lang="en">
<head>
<meta charset="utf-8">
<title>Brindle Cove, P.C. — Chico California Attorney</title>
<link href="https://fonts.googleapis.com/css2?family=Libre+Baskerville&family=Open+Sans:wght@400;600;700&display=swap" rel="stylesheet">
<style>
:root{
  --red:#ec1f27;
  --black:#000000;
  --white:#ffffff;
  --ink:#333333;
  --muted:#666666;
  --rule:#dddddd;
}
*{box-sizing:border-box;margin:0;padding:0}
html,body{width:1200px;height:3830px;overflow:hidden}
body{position:relative;background:var(--white);font-family:"Open Sans",Arial,sans-serif;color:var(--ink)}
.abs{position:absolute}
.center{text-align:center}

/* header */
.site-header{position:absolute;top:0;left:0;width:1200px;height:56px;background:var(--white);border-bottom:1px solid var(--rule)}
.brand{position:absolute;left:172px;top:6px;text-align:center;color:var(--red);font-family:"Libre Baskerville",Georgia,serif}
.brand-name{font-size:24px;line-height:28px;border-bottom:1px solid var(--red);padding:0 4px}
.brand-sub{font-size:11px;line-height:14px}
.main-nav{position:absolute;left:525px;top:0;display:flex;height:56px}
.main-nav a{display:block;padding:0 14px;line-height:56px;font-size:10px;font-weight:600;color:var(--muted);text-decoration:none;text-transform:uppercase;letter-spacing:.3px}
.main-nav a.current{color:var(--black);border-top:3px solid var(--red);line-height:50px}

/* hero */
.hero{position:absolute;top:56px;left:0;width:1200px;height:620px;background:radial-gradient(ellipse at 50% 60%,#7a7a7a 0%,#4a4a4a 55%,#2c2c2c 100%)}
.hero-title{position:absolute;top:330px;width:1200px;color:var(--white);font-weight:700;font-size:27px;text-transform:uppercase;letter-spacing:.3px}
.hero-text{position:absolute;top:378px;left:290px;width:620px;color:var(--white);font-size:12px;line-height:18px}

/* section headings */
.kicker{color:var(--red);font-size:20px;text-transform:uppercase;font-weight:400}
.subhead{font-family:"Libre Baskerville",Georgia,serif;font-size:19px;color:var(--muted)}
.subhead::before,.subhead::after{content:"";display:inline-block;width:30px;height:1px;background:var(--muted);vertical-align:middle;margin:0 18px}
.body-copy{font-size:11.5px;line-height:20px;color:var(--muted)}

/* dark bands */
.band{position:absolute;left:0;width:1200px;background:linear-gradient(90deg,#3a3a3a,#1e1e1e 50%,#3a3a3a)}

/* services */
.service{position:absolute;width:180px;text-align:center}
.diamond{width:64px;height:64px;margin:0 auto;transform:rotate(45deg);background:var(--white);box-shadow:0 2px 8px rgba(0,0,0,.18);display:flex;align-items:center;justify-content:center}
.diamond svg{transform:rotate(-45deg)}
.diamond.active{background:var(--red)}
.service-label{margin-top:34px;font-size:11px;font-weight:600;text-transform:uppercase;color:var(--black)}
.service-label.active{color:var(--red)}

/* testimonial */
.quote-icon{position:absolute;left:567px;top:2322px;width:66px;height:66px;border:2px solid var(--white);transform:rotate(45deg)}
.btn-outline{position:absolute;left:538px;top:2566px;width:124px;height:38px;border:1px solid var(--white);color:var(--white);font-size:11px;line-height:36px;text-align:center;text-transform:uppercase}

/* contact */
.contact-item{position:absolute;top:2818px;font-size:15px;color:var(--ink);display:flex;align-items:center;gap:12px}
.map-area{position:absolute;left:166px;top:2878px;width:860px;height:420px;background:radial-gradient(ellipse at 50% 50%,#e2e2e2 0%,#f0f0f0 60%,#ffffff 100%)}

/* ratings */
.badge{position:absolute;top:3425px}

/* footer */
.footer-bar{position:absolute;top:3560px;left:0;width:1200px;height:90px;background:var(--red)}
.footer-nav{position:absolute;left:150px;top:38px;display:flex}
.footer-nav a{color:var(--white);font-size:11px;text-decoration:none;padding:0 12px;border-left:1px solid rgba(255,255,255,.6)}
.footer-nav a:first-child{border-left:0}
.social{position:absolute;top:28px;width:34px;height:34px;border:1px solid var(--white);transform:rotate(45deg)}
.social.filled{background:var(--white)}
.footer-blurb{position:absolute;top:3672px;left:170px;width:860px;font-size:10px;line-height:16px;color:var(--ink)}
.footer-mark{position:absolute;left:591px;top:3740px;width:18px;height:18px;background:#cfcfcf;transform:rotate(45deg)}
.copyright{position:absolute;top:3800px;width:1200px;font-size:10px;color:var(--muted);text-align:center}
</style>
</head>
<body>

<header class="site-header">
  <div class="brand">
    <div class="brand-name">Brindle Cove</div>
    <div class="brand-sub">PC</div>
  </div>
  <nav class="main-nav">
    <a class="current">Home</a>
    <a>Attorney Profile</a>
    <a>Practice Areas ▾</a>
    <a>Client</a>
    <a>Reviews</a>
    <a>Links</a>
    <a>Contact</a>
  </nav>
</header>

<section class="hero" role="img" aria-label="Dimmed photo of a lawyer at a desk behind a word cloud of legal terms such as law, justice and legal"></section>
<h1 class="hero-title center">Business Law, Real Estate Law, Bankruptcy, Family Law, Etc</h1>
<p class="hero-text center">Call Attorney Maren T. Oakes to get the legal counsel you need to make important decisions. Our law firm approach is to work closely with clients to make sure they understand the legal process and related matters that apply to their case.</p>

<section>
  <h2 class="abs kicker center" style="top:764px;width:1200px">Brindle Cove, P.C.</h2>
  <p class="abs subhead center" style="top:800px;width:1200px">Chico California Attorney</p>
  <p class="abs body-copy center" style="top:866px;left:163px;width:874px">Find the big firm style legal counsel you can work with in your hometown region at Brindle Cove, P.C., in Chico, CA. Attorney Maren T. Oakes, Esq., offers a boutique law firm opportunity for clients who want to enjoy all the advantages of her broad legal experience and education. She works closely with clients, and has the knowledge of many areas of law to apply to your situation. This is very helpful when it is necessary to incorporate those different areas of law practice into creating a winning argument for your unique case.</p>
</section>

<section class="band" style="top:1085px;height:360px" role="img" aria-label="Dimmed photo of a speaker presenting to a seated audience"></section>
<h2 class="abs kicker center" style="top:1148px;width:1200px">Brindle Cove, P.C.</h2>
<p class="abs body-copy center" style="top:1220px;left:163px;width:874px;color:var(--white)">Brindle Cove P.C. is owned by Maren T. Oakes, a dedicated and caring professional who uses her broad range of skills as a California lawyer to bring consumers and business owners exceptionally strong legal representation that achieves best results. She works with people from across the northern region of California, from the Northern border to the Central Valley region. They bring her legal concerns and problems that occur in many areas of law, including Real Estate, Family law, Business Law, Bankruptcy, Criminal Law and Civil Litigation.</p>

<section>
  <h2 class="abs kicker center" style="top:1496px;width:1200px">Chico CA Law Firm</h2>
  <p class="abs body-copy center" style="top:1536px;width:1200px">At Brindle Cove, P.C., we offer the following clients services to help you manage all areas of your life that may need legal attention:</p>

  <div class="service" style="left:163px;top:1636px">
    <div class="diamond"><svg width="22" height="22" viewBox="0 0 22 22"><circle cx="11" cy="11" r="9" fill="none" stroke="#000" stroke-width="2"/><path d="M11 2a9 9 0 0 1 0 18z" fill="#000"/></svg></div>
    <div class="service-label">Business Law</div>
  </div>
  <div class="service" style="left:382px;top:1636px">
    <div class="diamond"><svg width="22" height="22" viewBox="0 0 22 22"><path d="M11 2a6 6 0 0 0-6 6c0 5 6 12 6 12s6-7 6-12a6 6 0 0 0-6-6z" fill="none" stroke="#000" stroke-width="2"/><circle cx="11" cy="8" r="2" fill="#000"/></svg></div>
    <div class="service-label">Real Estate Law</div>
  </div>
  <div class="service" style="left:587px;top:1636px">
    <div class="diamond active"><svg width="22" height="22" viewBox="0 0 22 22"><path d="M5 17L17 5M11 5h6v6" fill="none" stroke="#fff" stroke-width="2"/></svg></div>
    <div class="service-label active">Bankruptcy</div>
  </div>
  <div class="service" style="left:788px;top:1636px">
    <div class="diamond"><svg width="22" height="22" viewBox="0 0 22 22"><circle cx="11" cy="11" r="4" fill="none" stroke="#000" stroke-width="2"/><path d="M11 2v4M11 16v4M2 11h4M16 11h4M4.6 4.6l2.8 2.8M14.6 14.6l2.8 2.8M4.6 17.4l2.8-2.8M14.6 7.4l2.8-2.8" stroke="#000" stroke-width="2"/></svg></div>
    <div class="service-label">Family Law</div>
  </div>
  <div class="service" style="left:270px;top:1832px">
    <div class="diamond"><svg width="20" height="22" viewBox="0 0 20 22"><rect x="3" y="2" width="14" height="18" fill="none" stroke="#000" stroke-width="2"/><path d="M7 8h6M7 12h6" stroke="#000" stroke-width="2"/></svg></div>
    <div class="service-label">Criminal Law</div>
  </div>
  <div class="service" style="left:495px;top:1832px">
    <div class="diamond"><svg width="20" height="22" viewBox="0 0 20 22"><rect x="3" y="2" width="14" height="18" fill="none" stroke="#000" stroke-width="2"/><path d="M7 8h6M7 12h6" stroke="#000" stroke-width="2"/></svg></div>
    <div class="service-label">Civil Litigation</div>
  </div>
  <div class="service" style="left:709px;top:1832px">
    <div class="diamond"><svg width="20" height="22" viewBox="0 0 20 22"><rect x="3" y="2" width="14" height="18" fill="none" stroke="#000" stroke-width="2"/><path d="M7 8h6M7 12h6" stroke="#000" stroke-width="2"/></svg></div>
    <div class="service-label">Unlawful Detainer</div>
  </div>

  <p class="abs body-copy" style="top:2016px;left:163px;width:945px">When you encounter challenges in your personal or business matters, call Attorney Maren T. Oakes to get the legal counsel you need to make important decisions. Our law firm approach is to work closely with clients to make sure they understand the legal process and related matters that apply to their case. Our attitude is that every client is unique and deserves individual attention and solutions. From your first contact with our Chico CA Law Firm, you will feel welcomed and find the important answers you need. Our goal is to provide you with the knowledge you need to make informed decisions, no matter how large or small your case may be.</p>
  <p class="abs body-copy" style="top:2118px;left:163px;width:945px">Attorney Maren Oakes is ready to help you reach positive outcomes during mediation and arbitration meetings, around the real estate settlement tables, or inside the courtrooms of California. She will fight hard for your rights and help you manage your legal affairs. Buy, sell, lease or rent property, deal with</p>
</section>

<section class="band" style="top:2241px;height:432px" role="img" aria-label="Dimmed photo of two business people shaking hands across a table"></section>
<div class="quote-icon"></div>
<svg class="abs" style="left:588px;top:2343px" width="24" height="24" viewBox="0 0 24 24"><path d="M4 20l2-6L16 4l4 4-10 10z" fill="none" stroke="#fff" stroke-width="2"/></svg>
<h3 class="abs center" style="top:2396px;width:1200px;color:var(--white);font-size:22px;font-weight:400">Exceeded Our Expectations</h3>
<p class="abs body-copy center" style="top:2466px;left:230px;width:740px;color:var(--white)">Brindle Cove has met and exceeded our expectations in assisting our company with our real estate legal needs. In an area of law where the rules are ever changing, we simply could not navigate our company effectively without their help.</p>
<p class="abs center" style="top:2532px;width:1200px;color:var(--red);font-size:11px;text-transform:uppercase">Halvern Commercial</p>
<div class="btn-outline">Read More</div>

<section>
  <h2 class="abs kicker center" style="top:2740px;width:1200px">Contact</h2>
  <div class="contact-item" style="left:232px">
    <svg width="16" height="20" viewBox="0 0 16 20"><rect x="2" y="1" width="12" height="18" rx="2" fill="none" stroke="#333" stroke-width="2"/><circle cx="8" cy="15" r="1.3" fill="#333"/></svg>
    <span>(530) 555-0148</span>
  </div>
  <div class="contact-item" style="left:470px">
    <svg width="18" height="16" viewBox="0 0 18 16"><rect x="1" y="5" width="16" height="10" fill="#333"/><rect x="4" y="1" width="10" height="5" fill="none" stroke="#333" stroke-width="2"/></svg>
    <span>(888) 555-0192</span>
  </div>
  <div class="contact-item" style="left:696px">
    <svg width="18" height="14" viewBox="0 0 18 14"><rect x="1" y="1" width="16" height="12" fill="none" stroke="#333" stroke-width="1.5"/><path d="M1 1l8 7 8-7" fill="none" stroke="#333" stroke-width="1.5"/></svg>
    <span>Email: maren@brindlecovepc.com</span>
  </div>
  <div class="map-area" role="img" aria-label="Dotted world map marking the office location in Northern California"></div>
  <svg class="abs" style="left:370px;top:3028px" width="22" height="22" viewBox="0 0 22 22"><rect x="5" y="5" width="12" height="12" transform="rotate(45 11 11)" fill="#ec1f27"/></svg>
</section>

<section>
  <h2 class="abs kicker center" style="top:3354px;width:1200px;font-size:19px">Ratings and Reviews</h2>
  <svg class="badge" style="left:418px" width="86" height="100" viewBox="0 0 86 100"><path d="M4 4h78v62L43 96 4 66z" fill="#1f4e8c"/></svg>
  <svg class="badge" style="left:536px" width="96" height="100" viewBox="0 0 96 100"><circle cx="48" cy="50" r="44" fill="none" stroke="#444" stroke-width="3"/><circle cx="48" cy="50" r="32" fill="none" stroke="#444" stroke-width="1.5"/></svg>
  <svg class="badge" style="left:660px;top:3445px" width="130" height="60" viewBox="0 0 130 60"><rect x="2" y="2" width="126" height="56" fill="#e7e7e7"/></svg>
</section>

<footer>
  <div class="footer-bar">
    <nav class="footer-nav">
      <a>Home</a><a>Attorney Profile</a><a>Practice Areas</a><a>Client Reviews</a><a>Links</a><a>Contact Us</a>
    </nav>
    <div class="social" style="left:882px"></div>
    <div class="social" style="left:940px"></div>
    <div class="social filled" style="left:996px"></div>
  </div>
  <p class="footer-blurb center">Brindle Cove P.C. provides experienced, compassionate legal guidance and representation to businesses and individuals in the areas of business law, real estate law, bankruptcy, family law, criminal law, civil litigation, unlawful detainer, and legal document preparation. Located in Chico, California, we serve clients throughout Northern California including Butte County, Tehama County, Plumas County, Glenn County, Colusa County, Sutter County, Yuba County, Sierra County and Nevada County.</p>
  <div class="footer-mark"></div>
  <p class="copyright">Copyright © 2016 Brindle Cove, P.C. | Disclaimer | Site Map | Sign In</p>
</footer>

</body>
</html>
```